Velmor Stationery Design

We need Business Card, Letterhead, #10 Envelope , 3" x 4" Mailing Label, and email signature block. Also need "Aircraft Services" added small under the logo on everything except the email signature block. "Aircraft Services" should be in a simple font to to conflict with or distract from the logo. Our address info is:
4817 Halvend Loop NW
Brantwick, GA 30592
P 555.208.3146
C 555.208.3146 (for biz cards only)
glen@velmorjet.example (for biz cards only)
Website velmorjet.example
Feel free to play around with colors but I expect that black or gray will work best for the address/phone info etc.

Target Market(s)

Aircraft owners

Industry/Entity Type

Aviation

Colors

Designer to choose only greyscale colors for use in the design.

Requirements
Must have
• Clean and sophisticated design -

```html
<!DOCTYPE html>
<html lang="en">
<head>
<meta charset="utf-8">
<title>Velmor Email Signature</title>
<link rel="stylesheet" href="https://fonts.googleapis.com/css2?family=Figtree:wght@400;600;700&display=swap">
<style>
  :root {
    --canvas-bg: #e6e7e9;
    --card-bg: #ffffff;
    --brand-blue: #0079d9;
    --arc-gray: #8e8e8e;
    --text-dark: #3c3c3c;
    --text-light: #ffffff;
  }
  html, body {
    margin: 0;
    padding: 0;
    width: 1200px;
    height: 1200px;
    overflow: hidden;
    background: var(--canvas-bg);
  }
  .stage {
    width: 1200px;
    height: 1200px;
    display: flex;
    align-items: center;
    justify-content: center;
  }
  .signature {
    display: block;
    width: 1100px;
    height: 267px;
    background: var(--card-bg);
    box-shadow: 0 4px 14px rgba(0, 0, 0, 0.18);
    font-family: "Figtree", "Helvetica Neue", Arial, sans-serif;
  }
  .signature .person-name { fill: var(--brand-blue); font-weight: 600; font-size: 28px; }
  .signature .person-role { fill: var(--text-dark); font-weight: 400; font-size: 17px; letter-spacing: 0.3px; }
  .signature .contact-line { fill: var(--text-dark); font-weight: 400; font-size: 18px; }
  .signature .address-line { fill: var(--text-dark); font-weight: 400; font-size: 16.5px; }
  .signature .icon { fill: var(--brand-blue); }
  .signature .icon-stroke { fill: none; stroke: var(--brand-blue); stroke-width: 1.4; }
  .signature .brand-panel { fill: var(--brand-blue); }
  .signature .brand-arc { fill: var(--arc-gray); }
  .signature .brand-name { fill: var(--text-light); font-weight: 700; font-size: 50px; letter-spacing: 2px; }
</style>
</head>
<body>
<main class="stage">
  <svg class="signature" viewBox="0 0 737 179" role="group" aria-label="Velmor email signature">
    <!-- contact block -->
    <text class="person-name" x="47" y="47">FULL NAME</text>
    <text class="person-role" x="48" y="64">POSITION</text>

    <g class="contact-phone">
      <path class="icon" d="M50.5 80.5c1.2-1 2.3-.8 2.9.2l1.6 2.7c.5.9.2 1.8-.6 2.4l-1 .7c.7 2 2.4 3.9 4.4 4.9l.8-1c.6-.8 1.6-1 2.4-.4l2.6 1.7c1 .6 1.1 1.8.1 2.8l-1 1c-1.5 1.4-4.5.8-7.6-1.6-3.3-2.6-5.8-6.3-6.2-9.1-.2-1.4.2-2.5 1.1-3.4z"/>
      <text class="contact-line" x="72" y="95">P 555.208.3146</text>
    </g>

    <g class="contact-web">
      <circle class="icon-stroke" cx="56" cy="112" r="8.5"/>
      <ellipse class="icon-stroke" cx="56" cy="112" rx="3.8" ry="8.5"/>
      <line class="icon-stroke" x1="47.5" y1="112" x2="64.5" y2="112"/>
      <line class="icon-stroke" x1="49" y1="107.5" x2="63" y2="107.5"/>
      <line class="icon-stroke" x1="49" y1="116.5" x2="63" y2="116.5"/>
      <text class="contact-line" x="72" y="118">velmorjet.example</text>
    </g>

    <g class="contact-address">
      <path class="icon" d="M56 130c-4 0-7 3-7 6.8 0 4.8 7 13.2 7 13.2s7-8.4 7-13.2c0-3.8-3-6.8-7-6.8zm0 9.6a2.8 2.8 0 1 1 0-5.6 2.8 2.8 0 0 1 0 5.6z"/>
      <text class="address-line" x="72" y="143">4817 Halvend Loop NW</text>
      <text class="address-line" x="72" y="159">Brantwick, GA 30592</text>
    </g>

    <!-- brand panel -->
    <path class="brand-arc" d="M468 0 C404 25 360 110 371 179 L401 179 C386 120 420 20 478 0 Z"/>
    <path class="brand-panel" d="M478 0 C420 20 386 120 401 179 L737 179 L737 0 Z"/>
    <text class="brand-name" x="571" y="114" text-anchor="middle">VELMOR</text>
  </svg>
</main>
</body>
</html>
```